Business Card Design for Concierge business

Hi. I would like to have an elegant, smart business card for my concierge business, called Harbor Concierge. The services I provide are mail management, dog walking, cleaning, car, stylist, personal shopper, running errands, property management, event planning. I was thinking to add my picture but I would like to see options without it as well, if possible.

Thank you.

Business Card Details:
*Designers are to solely use contact information for the business card design. This is not to be used to contact the customer*

Name: Tamsin Heller
mail: quaylineerrands@mailvora.net
Phone: 305-482-9167

Target Market(s)

vacation home owners

Industry/Entity Type

Business

Font styles to use
Serif

Colors

Designer to choose colors to be used in the design.

Requirements
Nice to have
• Could use icons that describe the services I provide for example car, house, key, shopping cart, shopping bags, envelope, champagne glasses, phone, dog etc.

```html
<!DOCTYPE html>
<html lang="en">
<head>
<meta charset="utf-8">
<title>Harbor Concierge – Business Card</title>
<link rel="stylesheet" href="https://fonts.googleapis.com/css2?family=Cinzel:wght@400;600&family=Open+Sans:wght@400&display=swap">
<style>
  :root{
    --bg:#e9e7e4;
    --card-front:#f7f7f7;
    --card-back:#0b0b0b;
    --ink:#161616;
    --ink-soft:#333333;
    --white:#ffffff;
    --gold:#b8955a;
    --photo-a:#d9d6d2;
    --photo-b:#6b5a52;
  }
  *{box-sizing:border-box;margin:0;padding:0}
  html,body{width:1200px;height:844px;overflow:hidden;background:var(--bg)}
  .stage{position:relative;width:1200px;height:844px;display:flex;align-items:center;justify-content:center;gap:40px}
  .card{position:relative;width:520px;height:300px;overflow:hidden;box-shadow:0 10px 28px rgba(0,0,0,.18)}
  .card-front{background:var(--card-front)}
  .portrait{position:absolute;left:24px;bottom:0;width:210px;height:262px;border-radius:100px 100px 0 0;
    background:linear-gradient(180deg,var(--photo-b) 0%,var(--photo-a) 35%,var(--photo-b) 100%)}
  .brand{position:absolute;left:266px;top:44px;width:230px;font-family:"Cinzel",serif;font-weight:400;font-size:26px;line-height:1.15;letter-spacing:3px;color:var(--ink);text-align:center}
  .brand span{display:block}
  .holder{position:absolute;left:268px;top:156px;font-family:"Cinzel",serif;font-weight:600;font-size:17px;letter-spacing:.5px;color:var(--ink)}
  .contact{position:absolute;left:268px;top:192px;list-style:none;font-family:"Open Sans",sans-serif;font-size:12.5px;color:var(--ink-soft)}
  .contact li{display:flex;align-items:center;gap:8px;margin-bottom:5px;white-space:nowrap}
  .contact svg{width:11px;height:11px;fill:var(--ink)}
  .card-back{background:var(--card-back);display:flex;flex-direction:column;align-items:center;padding-top:62px}
  .services-title{font-family:"Cinzel",serif;font-weight:400;font-size:30px;color:var(--white);letter-spacing:1px}
  .rule{width:210px;height:1px;background:var(--gold);margin:10px 0 14px}
  .services{list-style:none;text-align:center;font-family:"Open Sans",sans-serif;font-size:15.5px;line-height:1.55;color:var(--white)}
</style>
</head>
<body>
<main class="stage">
  <section class="card card-front">
    <div class="portrait" role="img" aria-label="Portrait photo of Tamsin Heller"></div>
    <div class="brand"><span>Harbor</span><span>Concierge</span></div>
    <h1 class="holder">Tamsin Heller</h1>
    <ul class="contact">
      <li><svg viewBox="0 0 24 24" aria-hidden="true"><path d="M6.6 10.8a15 15 0 0 0 6.6 6.6l2.2-2.2c.3-.3.7-.4 1-.2 1.1.4 2.3.6 3.6.6.6 0 1 .4 1 1V20c0 .6-.4 1-1 1A17 17 0 0 1 3 4c0-.6.4-1 1-1h3.5c.6 0 1 .4 1 1 0 1.3.2 2.5.6 3.6.1.3 0 .7-.2 1z"/></svg>305-482-9167</li>
      <li><svg viewBox="0 0 24 24" aria-hidden="true"><path d="M2 5h20v14H2z M4 7v.5l8 5 8-5V7l-8 5z" fill-rule="evenodd"/></svg>quaylineerrands@mailvora.net</li>
    </ul>
  </section>
  <section class="card card-back">
    <h2 class="services-title">Our Services</h2>
    <div class="rule"></div>
    <ul class="services">
      <li>Mail Management | Dog Walking</li>
      <li>Cleaning | Car | Stylist</li>
      <li>Personal Shopper | Running Errands</li>
      <li>Property Management | Event Planning</li>
    </ul>
  </section>
</main>
</body>
</html>
```